Membership Drive "End of Spring Sale"

Looking to run a Direct Debit Sale for November 2019 to boost membership number up. This is our slowest area for membership growth, many choose not to do direct debit, special is designed to increase numbers. Artwork will be display via social media (FB and Instagram) as well as in store. Artwork must be eye catching and direct to the customer. Customer should feel a sense of relief with monthly payments instead of one large payment.

Heading: "End of Spring Special"
Direct Debit
$39.95 per month
Terms and conditions apply"
*Offer End 30th November

Slogan:
"More Energy
More Atmosphere
Feel the Difference
Make the change now" can be placed where suits.

below are other promos we had designed on Artwork Hive along with potential photos to be included into this promo

Target Market(s)

Males and Females aged between 18 - 40

Industry/Entity Type

Fitness

Colors

Designer to choose colors to be used in the design.

Requirements
Must have
• Must emphasize "End of Spring Special" $39.95 per month and
• under neath strict terms and conditions apply
• Offer Ends 30th of November
• "All of our contact details"
• Address: 14 Marlow Rd Brindle Park 3187
• Ph: 9581 2706
• www.pulsarfit.com.au
• Design format must come in poster size A0 size, Instagram format, Facebook cover and 800 x 800 for the website
Nice to have
• With the photos attached at least one female and one male in the overall design. Lots of color in relation to Spring and artistic effects to catch peoples eyes.
• Also to include "Celebrating 49 years"

```html
<!DOCTYPE html>
<html lang="en">
<head>
<meta charset="utf-8">
<title>Pulsar Fit – End of Spring Special</title>
<link rel="stylesheet" href="https://fonts.googleapis.com/css2?family=Anton&family=Oswald:wght@700&display=swap">
<style>
  :root {
    --black: #050505;
    --red: #e41c23;
    --yellow: #fcd45f;
    --white: #ffffff;
    --photo-warm: #6b3a24;
    --photo-dark: #1a1412;
  }
  * { margin: 0; padding: 0; box-sizing: border-box; }
  html, body { width: 849px; height: 1200px; overflow: hidden; background: var(--black); }
  .poster {
    position: relative; width: 849px; height: 1200px; overflow: hidden;
    background: var(--black);
    font-family: "Anton", "Oswald", sans-serif;
    text-transform: uppercase;
  }
  .photo { position: absolute; }
  .photo--female {
    left: 0; top: 0; width: 460px; height: 545px;
    background: radial-gradient(ellipse at 40% 40%, var(--photo-warm) 0%, #2b1810 55%, var(--black) 90%);
  }
  .photo--male {
    left: 300px; top: 565px; width: 490px; height: 580px;
    background: radial-gradient(ellipse at 50% 40%, #7a4a30 0%, #3a2a24 45%, var(--photo-dark) 75%, var(--black) 100%);
  }
  .brand {
    position: absolute; left: 641px; top: 1px; width: 184px; height: 184px;
    border: 3px solid var(--white); border-radius: 50%;
    display: flex; align-items: center; justify-content: center;
    color: var(--white); font-size: 34px; letter-spacing: 1px;
  }
  .headline { position: absolute; color: var(--yellow); line-height: 1; }
  .headline--top { left: 428px; top: 128px; font-size: 76px; }
  .headline--main { left: 84px; top: 206px; font-size: 114px; letter-spacing: -1px; }
  .band { position: absolute; left: 0; top: 0; width: 849px; height: 1200px; }
  .band polygon { fill: var(--red); }
  .price {
    position: absolute; left: 30px; top: 520px;
    transform: rotate(-14deg); transform-origin: left top;
    white-space: nowrap;
  }
  .price__amount { color: var(--white); font-size: 98px; line-height: 1; display: inline-block; }
  .price__unit { color: var(--yellow); font-size: 36px; display: inline-block; vertical-align: 26px; margin-left: 4px; }
  .price__terms {
    position: absolute; left: 130px; top: 92px;
    font-family: "Oswald", sans-serif; font-weight: 700; text-transform: none;
    color: var(--black); font-size: 20px;
  }
  .deadline {
    position: absolute; left: 498px; top: 430px;
    transform: rotate(-14deg); transform-origin: left top;
    text-transform: none; line-height: 1.1; text-align: center; white-space: nowrap;
  }
  .deadline__line { color: var(--yellow); font-size: 38px; display: block; }
  .deadline__date { color: var(--white); }
  .anniversary { position: absolute; right: 35px; top: 624px; text-align: right; line-height: 1.3; font-size: 50px; color: var(--white); }
  .anniversary__num { color: var(--red); font-size: 58px; }
  .slogan { position: absolute; left: 52px; top: 768px; list-style: none; }
  .slogan li { font-size: 64px; line-height: 84px; }
  .slogan .accent { color: var(--red); }
  .slogan .plain { color: var(--white); }
  .footer {
    position: absolute; left: 0; top: 1143px; width: 849px; height: 57px;
    background: var(--red);
    display: flex; align-items: center; gap: 14px; padding: 0 22px;
  }
  .footer__tab { position: absolute; top: -8px; height: 8px; background: var(--red); }
  .footer__item { display: flex; align-items: center; gap: 12px; color: var(--black); font-size: 23px; margin-right: 16px; }
  .footer__item svg { width: 26px; height: 30px; flex: none; }
</style>
</head>
<body>
<main class="poster">
  <div class="photo photo--female" role="img" aria-label="Woman with ponytail pulling a cable machine bar"></div>
  <div class="photo photo--male" role="img" aria-label="Muscular man lifting weight plates in a dark gym"></div>

  <div class="brand">Pulsar Fit</div>

  <h1>
    <span class="headline headline--top">End of</span>
    <span class="headline headline--main">Spring Special</span>
  </h1>

  <svg class="band" viewBox="0 0 849 1200" aria-hidden="true">
    <polygon points="0,555 491,431 441,570 0,690"/>
    <polygon points="502,431 849,338 849,470 455,570"/>
  </svg>

  <div class="price">
    <span class="price__amount">$39.95</span><span class="price__unit">Month</span>
    <span class="price__terms">Terms and conditions apply</span>
  </div>

  <div class="deadline">
    <span class="deadline__line">Offer Ends</span>
    <span class="deadline__line"><span class="deadline__date">30th</span> of November</span>
  </div>

  <div class="anniversary">
    Celebrating<br><span class="anniversary__num">49</span> Years
  </div>

  <ul class="slogan">
    <li class="accent">More Energy</li>
    <li class="plain">More Atmosphere</li>
    <li class="accent">Feel the Difference</li>
    <li class="plain">Make the change now</li>
  </ul>

  <footer class="footer">
    <span class="footer__tab" style="left:0;width:140px"></span>
    <span class="footer__tab" style="left:330px;width:190px"></span>
    <span class="footer__tab" style="left:700px;width:149px"></span>
    <span class="footer__item">
      <svg viewBox="0 0 26 30" aria-hidden="true"><path d="M13 2a9 9 0 0 0-9 9c0 7 9 15 9 15s9-8 9-15a9 9 0 0 0-9-9z" fill="none" stroke="#fff" stroke-width="2.5"/><circle cx="13" cy="11" r="3" fill="#fff"/><path d="M3 28h20" stroke="#fff" stroke-width="2.5"/></svg>
      14 Marlow Rd Brindle Park 3187
    </span>
    <span class="footer__item">
      <svg viewBox="0 0 26 30" aria-hidden="true"><path d="M7 3l4 6-3 3c1 4 4 7 7 8l3-3 6 4-3 5C12 25 3 16 3 6z" fill="#fff"/></svg>
      9581 2706
    </span>
    <span class="footer__item">
      <svg viewBox="0 0 30 30" aria-hidden="true"><g fill="none" stroke="#fff" stroke-width="2"><circle cx="15" cy="15" r="12"/><ellipse cx="15" cy="15" rx="5" ry="12"/><path d="M3 15h24M5 9h20M5 21h20"/></g></svg>
      pulsarfit.com.au
    </span>
  </footer>
</main>
</body>
</html>
```